Catastrophe & Disaster Mitigation & Repairs

1. Fire/smoke & flood/water & wind damage restoration for residential, commercial or industrial structure &/or content.

2. 24/7 emergency service

3. Flood, catastrophe & storm emergency response

4. Emergency board ups.

5. Specializing in insurance claims with direct insurance billing (when applicable).

6. Full service restoration. We handle everything from cleaning & deoderization of content & structure, demo, drying, disposal & dry cleaning to temporary storage, emergency electrical & plumbing & FULL repairs "To Restore residential or commercial property & content to pre loss condition".

7. Please see our website, brochure or simply ask any of our technicians for complete list of services & specialized services that we provide.

However within 60 to 90 days after we incorporate & launch this new business we are starting a sister company that will handle all of the carpentry & construction on all of our insurance jobs as well as market for additional roofing, siding, interiors, exterior, kitchens, baths, additions, painting, insulation, drywall, doors, windows, decks, additions, garages, general contracting, electrical, hardwood floor restoration & instalation, custom tile, vinyl, carpet & laminate flooring installation, tree houses, small concrete repairs, brick repair, doors, windows, new builds, etc, etc. When the time comes I will need business card, rak cards, note books, stickers, yard signs, vehicle magnets, etc for that business (Steadfast Building Services) too. So please keep in mind that we can temporarily have construction & full repairs on this card but in the near future the majority of anything carpentry or construction related (aside from demo) will need to be easily removes from this card and replaced with a brief line referring to the sister company.

We have a long long long list of services that we provide for residential, commercial & industrial. Duct cleaning & sanitize, foreclosure clean out, pre & post rental or sale cleaning &/or repairs & painting, home & office cleaning services, post construction clean up, crime scene remediation, smoke & odor removal & mitigation, residential cleaning, commercial cleaning, water proofing, biohazard clean up, septic back up clean up, temporary power, temporary heat, temporary storage, temporary repairs, refrigerant & desiccant & heat drying, mold mitigation (we don't like mold & don't advertise for mold but are educated, trained & equipped to do it upon request or nessecity), full pack out of content, full move back, demo & disposal, indoor air quality testing, consulting, claim negotiation with insurance carrier, content cleaning & restoration, jewelry cleaning, dry cleaning, pressure washing, steam pressure washing, sand & dry ice blasting, graffiti removal, inventory of damaged, destroyed & cleaned content, upholstery & carpet cleaning, grout cleaning, property winterizing, soda blasting, art & document restoration, emergency & long term utility reactivate,
landscaping & clean up of property/yard damaged as result of catastrophe (if covered in policy or upon request), wind or catastorphe damaged tree cut up & removal, project management or consulting, some equipment rental, pump outs, water extraction, electronics cleaning, bat guanno removal & mitigation, mitigation & remediation planning, detailed & itemized written estimates with industry standard pricing software, spring cleaning, hordar clean outs, garage/attic/basement & barn clean out & hauloff, RV clean out, full demo & removal of total loss or condemned structures, no intrest payment plans for the unfortunate & uninsured (with sizeable down payment). I know there are more services that I'm not thinking of too.

When a less than once in a lifetime castorphe strikes a home, business, commercial or industrial structure & often times the content of that structure the owners are often in shock & don't know what direction to turn or where to begin simply because they most likely have never been through a loss of that magnitude & in very unfamiliar territory. The amount of planning, equipment, training, networking, resources, subcontractors, manpower, financing & paperwork can be mindboggling. Especially when the majority of them have jobs, school, family & lives that don't stop due to their misfortune. Keystone Water & Blaze Recovery LLC handles every aspect from before the time first responders or plumbers are gone until the structure & content is restored to (or better than) preloss condition. They only thing we need from our customers is for them to provide us with material kind & color such as paint & flooring. Aside from that, our customers can go on with there lives and have as little stress & worry as possible given the circumstances. From a small over flowed sink to a large warehouse fire that sets of a high pressure sprinkler system to a structure that's been completely sumburged for several days it is still uncommon territory & still requires a lot of different skilled subcontractors, specialized equipment & logistics. Its what we do every day & we have it well planned in advance, a core team of dedicated & trusted professionals that we've been colleges & friends with for years. The homeowners are still our direct customer & are consulted on every aspect of mitigation & repairs to their home, property &/or content. Our customers are free to choose what (if any) aspects of the project they handle themselves. From time to time they choose to paint their own bedroom or have a friend or family member that's a electrician, plumber or tradesman & chose to use them for that portion of their loss. Point being that even though we can handle every aspect we still work closely with our customers & even if direct insurance invoicing the policy holder/home or structure owner is still our valued customer. We also do as much as we can to get their lives back to as fully functional as possible given the circumstance.

As I'm sure you can tell.... I've provided a lot of text. Please save some for the rack cards, brochures, folders and anything else you may be able to use it in. I have a ton more of informational text from our old website. I also have a lot of testimonials, photos & anything else you may be able to implement in our promotional & informative campaign. We've been in this business for 8 years, in the flood & fire restoration business for 11 years as well as having well over 100 years combined experience in the carpentry & constructive fields. At some point & on something I'd like all our services listed. Maybe on brochures. I attached the brochure that my cousin (who at the time was graphics editor at Vortell Magazine) designed when we first got in business. Its a quality job but I feel is very outdated & not very informative.
I understand that I have just a few seconds to catch my potential customers eye so I feel with the business cards that one side needs to POP, be clean, look good and stand out at you and the other side can list some of our services. I think that #'s 1 thru 7 at the top of this section should be most of it for the back of the business card. Please look through this not so brief, brief & see what you think. I'm gearing towards fire, smoke, flood & wind mitigation. Then cleaning + emergency, storm & catastrophe response.
The biggest thing is that it needs to make both of my competitors attached cards look like shit & unfortunately I kinda like both of their cards so you have your work cut out for you. One of the reasons I gave you such extensive information. Please keep rack cards, brochures, letter heads, envelopes, notebooks, folders, informative literature, documents, stickers, door magnets & everything else we may need for both this & construction business. I'll be able to pay for that next week. I also keep clicking on Double Sided & it keeps changing back to single by itself.
Updates

PLEASE NOTE THAT I SUBMITTED FOR "BUSINESS CARD DESIGN" THERE WASNT A OPTION FOR EXACTLY WHAT I NEED HELP WITH. I NEED MY EXISTING LOGO MODIFIED ALONG WITH THE BUSINESS CARD DESIGN. I ALSO NEED A BROCHURE & RACK CARD DESIGNED. I'D LIKE TO DO ALL OF THIS ASAP. PLEASE LET ME KNOW THE CHARGES FOR THESE ADDITIONAL SERVICES. THANK YOU.

Target Market(s)

Insurance agents, insurance adjusters, homeowners/policy holders that have experienced a fire, flood or other catastorphies, plumbers, builders, etc

Industry/Entity Type

Office Cleaning

Contact Information for Business Card

Reed Talbot
Keystone Water & Blaze Recovery LLC
5318 Whitcombe Rd
Mayville, NY 14092
www.keystonewaterblaze.example
reed@keystonewaterblaze.example
Office: 716.555.0142
Cell: 716.555.0187

Requirements
Must have
• I've attached a copy of our old business & logo as well as a old business card. I'd like to incorporate our old logo & colors. Or at least entertain using them in some aspect. Feel free to change it up though. Our old logo is supposed to represent a roof & the red for fire & blue for water.

My old card is cluttered & doesn't catch the eye.

The other cards I've attached are Grip on Spores who is my old business partner from years ago & Lakeshore Basin Renewal is my ex fiance so my new cards don't just need to catch the eye & be functional they need to look at least twice as good as my competitors.
Nice to have
• One side business name, my name, logo, phone #'s, email, website, fb, twitter, instagram, etc. I feel one side should be clean, bold & catch the eye in the 6 seconds I have to do so.

Then opposing side should have some of our more prominent services along with more information.

I'd like to keep away from having the business cards on white card stock. I think a color or multi color looks better.

I guess I'm open to anything. You guys are the pro's. As long as it looks great & gets the point across. I have 2 other people that need the same cards too. Just different names, emails & cell #'s. And as I stated earlier. I'm planning on ordering notepads, yard signs, rack cards, brochures, magnets & a few other things at the same time. I'll need design & layout on all of those too. Just let me know what the additional cost will be. They'll have the same colors, logo & business name. Just more or less info depending on the product.
Should not have
• ?

```html
<!DOCTYPE html>
<html lang="en">
<head>
<meta charset="utf-8">
<title>Reed Talbot – Keystone Water &amp; Blaze Recovery</title>
<link rel="stylesheet" href="https://fonts.googleapis.com/css2?family=Lobster&family=Alfa+Slab+One&family=Arimo:wght@400;700&family=Roboto+Condensed:wght@700&display=swap">
<style>
  :root {
    --brand-blue: #0b7fc0;
    --text-blue: #1b86c6;
    --band-light: #dcebf5;
    --band-dark: #b7d3e6;
    --ink-grey: #3b3b3d;
    --water: #2a8fd8;
    --fire: #d2452a;
    --wind: #c42a2a;
    --smoke: #b32626;
    --tile-top: #1d1f22;
    --white: #ffffff;
  }
  * { margin: 0; padding: 0; box-sizing: border-box; }
  html, body { width: 1050px; height: 1200px; overflow: hidden; background: var(--white); }
  .card { position: relative; width: 1050px; height: 1200px; background: var(--white); overflow: hidden; }

  .hero {
    position: absolute; left: 0; top: 0; width: 1050px; height: 600px;
    background:
      linear-gradient(135deg, rgba(255,255,255,0) 0%, rgba(255,255,255,0) 68%, rgba(255,255,255,.35) 68%, rgba(255,255,255,.35) 100%),
      repeating-linear-gradient(180deg, var(--band-light) 0 14px, var(--band-dark) 14px 22px);
  }
  .hero::after {
    content: ""; position: absolute; inset: 0;
    background: radial-gradient(ellipse at 50% 45%, rgba(255,255,255,.55), rgba(255,255,255,0) 60%);
  }

  .brand { position: absolute; left: 0; top: 100px; width: 1050px; text-align: center; z-index: 1; }
  .brand-dot {
    display: block; width: 190px; height: 190px; margin: 0 auto;
    border-radius: 50%; background: var(--brand-blue);
  }
  .brand-name {
    display: block; margin-top: 28px;
    font-family: "Arimo", sans-serif; font-weight: 700; font-size: 64px;
    color: var(--ink-grey); letter-spacing: 2px; line-height: 1;
  }

  .hazards { position: absolute; top: 423px; left: 0; width: 1050px; height: 116px; z-index: 1; }
  .hazard {
    position: absolute; width: 103px; height: 116px; border-radius: 12px;
    border: 4px solid #8c9298; overflow: hidden;
    display: flex; align-items: flex-end; justify-content: center;
    font-family: "Roboto Condensed", sans-serif; font-weight: 700; font-size: 24px;
    color: var(--white); padding-bottom: 10px;
  }
  .hazard--water { left: 210px; background: linear-gradient(180deg, var(--tile-top) 0 45%, var(--water) 75%); }
  .hazard--fire  { left: 386px; background: linear-gradient(180deg, var(--tile-top) 0 45%, var(--fire) 75%); }
  .hazard--wind  { left: 566px; background: linear-gradient(180deg, var(--tile-top) 0 45%, var(--wind) 75%); }
  .hazard--smoke { left: 736px; background: linear-gradient(180deg, #555 0 40%, var(--smoke) 75%); }

  .availability {
    position: absolute; left: 50px; top: 690px; width: 240px; text-align: center;
    font-family: "Lobster", cursive; color: var(--brand-blue); white-space: nowrap;
  }
  .availability-hours { font-size: 52px; line-height: 50px; }
  .availability-line { font-size: 24px; line-height: 28px; }

  .tagline {
    position: absolute; left: 500px; top: 660px; width: 520px; text-align: center;
    font-family: "Lobster", cursive; font-weight: 400; font-size: 50px; line-height: 74px;
    color: var(--brand-blue); white-space: nowrap;
  }

  .person {
    position: absolute; left: 0; top: 868px; width: 1050px; text-align: center;
    font-family: "Alfa Slab One", serif; font-weight: 400; font-size: 48px; line-height: 60px;
    color: var(--brand-blue); letter-spacing: 1px;
  }

  .services {
    position: absolute; left: 46px; top: 1040px; width: 436px;
    font-family: "Roboto Condensed", sans-serif; font-weight: 700; font-size: 16px;
    letter-spacing: 0.9px; line-height: 30px; color: var(--text-blue);
    text-align: justify; text-align-last: left;
  }

  .contact { position: absolute; left: 668px; top: 1016px; width: 380px; }
  .contact-row { position: relative; height: 50px; padding-left: 64px; }
  .contact-icon { position: absolute; left: 0; top: 2px; width: 40px; height: 36px; }
  .contact-text {
    font-family: "Arimo", sans-serif; font-size: 15px; line-height: 20px;
    color: var(--text-blue); white-space: nowrap;
  }
</style>
</head>
<body>
<main class="card">
  <section class="hero">
    <div class="brand">
      <span class="brand-dot"></span>
      <span class="brand-name">KWBR</span>
    </div>
    <div class="hazards">
      <div class="hazard hazard--water" role="img" aria-label="Water damage icon: blue water drop">Water</div>
      <div class="hazard hazard--fire" role="img" aria-label="Fire damage icon: orange flame">Fire</div>
      <div class="hazard hazard--wind" role="img" aria-label="Wind damage icon: red storm swirl">Wind</div>
      <div class="hazard hazard--smoke" role="img" aria-label="Smoke damage icon: grey smoke cloud">Smoke</div>
    </div>
  </section>

  <div class="availability">
    <div class="availability-hours">24/7</div>
    <div class="availability-line">Emergency service</div>
    <div class="availability-line">Emergency board ups.</div>
  </div>

  <h1 class="tagline">Catastrophe &amp; Disaster<br>Mitigation &amp; Repairs</h1>

  <h2 class="person">REED TALBOT</h2>

  <p class="services">Fire/smoke &amp; flood/water &amp; wind damage restoration for residential, commercial or industrial structure &amp;/or content. Specializing in insurance claims with direct insurance billing (when applicable).</p>

  <div class="contact">
    <div class="contact-row">
      <svg class="contact-icon" viewBox="0 0 40 36" aria-hidden="true">
        <circle cx="20" cy="18" r="15" fill="none" stroke="var(--text-blue)" stroke-width="1.5"/>
        <path d="M15 10c-2 2-2 6 1 10s7 7 10 6l2-2-3-3-2 1c-2-1-4-4-5-6l1-2-3-3z" fill="none" stroke="var(--text-blue)" stroke-width="1.5"/>
      </svg>
      <div class="contact-text">Cell &nbsp;&nbsp;: 716-555-0187<br>Office: 716-555-0142</div>
    </div>
    <div class="contact-row">
      <svg class="contact-icon" viewBox="0 0 40 36" aria-hidden="true">
        <path d="M3 7h14c2 0 3 1 3 3v20c0-2-1-3-3-3H3z M37 7H23c-2 0-3 1-3 3v20c0-2 1-3 3-3h14z" fill="none" stroke="var(--text-blue)" stroke-width="1.5"/>
      </svg>
      <div class="contact-text">Keystone Water &amp; Blaze Recovery<br>LLC 5318 Whitcombe Rd Mayville, NY 14092</div>
    </div>
    <div class="contact-row">
      <svg class="contact-icon" viewBox="0 0 40 36" aria-hidden="true">
        <rect x="8" y="6" width="24" height="18" fill="none" stroke="var(--text-blue)" stroke-width="1.5"/>
        <path d="M4 30h32l-3-5H7z" fill="none" stroke="var(--text-blue)" stroke-width="1.5"/>
      </svg>
      <div class="contact-text">reed@keystonewaterblaze.example<br>www.keystonewaterblaze.example</div>
    </div>
  </div>
</main>
</body>
</html>
```